Writer needs an exciting Cover for a new eBook

I am a new writer looking to embark on launching my first eBook. I'm looking for a designer to help me build an exciting cover. I've outlined the project objective and description.
Objective: Create an eBook cover for my new eBook.
Outlined below is an overview of the genre of the eBook as well as a brief on the style of the cover that may be most appropriate. Cover dimensions are included at the end of the brief.
eBook Genre: Erotica
1st eBook:
Title: Velvet Hours
This erotica eBook has 9 chapters with each chapter focusing on a different encounter with a man from a different background. Chapters will be denoted as the man’s background ‘The Italian’, ‘The Romanian’.
Written in the female voice, it outlines Marla’s steamy encounters into a world of sexual self-discovery.
I envision the cover being all black with a couple in the background but muted so you can make out the outline of their bodies but you can’t fully see them. The couple should be in a steamy embrace and if possible they would be nude. Again you wouldn’t be able to see the bodies with great details.
Over the image the title would appear ‘Velvet Hours’. I envision the font type of the title to be strong, potentially bolded in white or red font.
Running along the very bottom of the cover I’d like to add an eBook descriptor:
Enormously intense and fun read.
To make this area stand out I’d put it in a band of colour – maybe white with black font running along the bottom.
eBook Site Specs:
Two types of files for cover images are acceptable (prefer jpg):
JPEG (.jpeg / .jpg)
TIFF (.tif /.tiff)
We apply additional compression to images when displaying them on the website. For best results, please upload your images with minimal compression.
Dimensions
Requirements for the size of your cover art must have an ideal height/width ratio of at least 1.6, meaning:
• A minimum of 625 pixels on the shortest side and 1000 pixels on the longest side
• For best quality, your image should be 2500 pixels on the longest side
Important: We cannot accept any image larger than 10,000 pixels on the longest side.
Size
Your cover image must be less than 50MB. If the file type you are using supports compression, make sure to enable as little compression as possible, e.g. none for TIFF. Be sure to save your file with 72 dots per inch (dpi).
Color
Product images display on the Brindle website using the RGB (red, green, blue) color mode or profile. RGB is the color mode native to the web and many color screen displays, as these three colors displayed at varying levels of intensity create over 16 million colors. When saving and uploading your cover image file, save your file ONLY as RGB - not CMYK or sRGB- for the color profile. You can usually find this option in the File saving dialog of image manipulation programs such as Photoshop.
Some programs may also refer to RGB color as 'True Color' in some programs. If in doubt, try opening a JPG inside Internet Explorer, Firefox, or Safari. If a JPG opens fine inside a web browser, it's most likely OK to use as a cover image.
Make sure to save your image without color separation. This is usually a pre-press or color palette option. Use your image manipulation program or image analysis tool (some are freely available online) to verify that your image file doesn't have color separation.
Use color images whenever possible and relevant. In addition to the Quillo black and white e-ink reading devices, customers can read your books on full color Lumo devices and free-to-download Quillo reading apps for Zentaphone, Zentatab, Korvex, PC or Olt.
Borders for White Cover Art
Cover art with white or very light backgrounds can seem to disappear against the white background. Adding a very narrow (3-4 pixel) border in medium gray will define the boundaries of the cover.
Females that read erotica regularly. It should welcome those that are newly exploring erotica for the first time as well. (should not feel overwhelming or intimidating).

```html
<!DOCTYPE html>
<html lang="en">
<head>
<meta charset="utf-8">
<title>Velvet Hours — eBook Cover</title>
<link href="https://fonts.googleapis.com/css2?family=Oswald:wght@300;400&family=Open+Sans:wght@700&display=swap" rel="stylesheet">
<style>
  :root {
    --ink: #000000;
    --ember-deep: #3a0805;
    --ember: #8a1a0c;
    --ember-bright: #c2391a;
    --flame: #f07a2a;
    --title-red: #d42a14;
    --subtitle-mauve: #8a4a50;
    --tagline: #ffffff;
  }
  html, body {
    margin: 0;
    padding: 0;
    width: 750px;
    height: 1200px;
    overflow: hidden;
    background: var(--ink);
  }
  .cover {
    position: relative;
    width: 750px;
    height: 1200px;
    overflow: hidden;
    background: linear-gradient(180deg, var(--ink) 0%, var(--ink) 70%, #1a0a0a 100%);
  }
  .couple-photo {
    position: absolute;
    inset: 0;
    background:
      radial-gradient(ellipse 30% 22% at 32% 22%, rgba(194,57,26,0.75), rgba(194,57,26,0) 70%),
      radial-gradient(ellipse 26% 24% at 58% 32%, rgba(150,36,16,0.7), rgba(150,36,16,0) 70%),
      radial-gradient(ellipse 42% 40% at 45% 62%, rgba(138,26,12,0.8), rgba(58,8,5,0) 75%),
      radial-gradient(ellipse 40% 20% at 50% 92%, rgba(70,14,10,0.6), rgba(0,0,0,0) 80%);
  }
  .title {
    position: absolute;
    left: 0;
    top: 0;
    width: 750px;
    height: 1200px;
  }
  .title-main {
    font-family: "Oswald", sans-serif;
    font-weight: 300;
    font-size: 300px;
    fill: url(#titleGlow);
    opacity: 0.85;
  }
  .title-sub {
    font-family: "Oswald", sans-serif;
    font-weight: 400;
    font-size: 96px;
    fill: var(--subtitle-mauve);
    opacity: 0.8;
  }
  .tagline {
    position: absolute;
    left: 0;
    right: 0;
    top: 1120px;
    margin: 0;
    text-align: center;
    font-family: "Open Sans", sans-serif;
    font-weight: 700;
    font-size: 13px;
    letter-spacing: 0.4px;
    color: var(--tagline);
    text-transform: uppercase;
  }
</style>
</head>
<body>
  <main class="cover">
    <div class="couple-photo" role="img" aria-label="Muted red-toned photograph of a nude couple in a steamy embrace against a black background"></div>

    <svg class="title" viewBox="0 0 750 1200" aria-labelledby="bookTitle">
      <title id="bookTitle">Velvet Hours</title>
      <defs>
        <linearGradient id="titleGlow" x1="0" y1="0" x2="1" y2="0">
          <stop offset="0" stop-color="#b8220f"/>
          <stop offset="0.3" stop-color="#f07a2a"/>
          <stop offset="0.6" stop-color="#c2391a"/>
          <stop offset="1" stop-color="#7a4a4a"/>
        </linearGradient>
      </defs>
      <text class="title-main" x="78" y="918" textLength="584" lengthAdjust="spacingAndGlyphs">VELVET</text>
      <text class="title-sub" x="82" y="1002" textLength="578" lengthAdjust="spacingAndGlyphs">HOURS</text>
    </svg>

    <p class="tagline">An enormously intense and fun read</p>
  </main>
</body>
</html>
```